Brellify Sponsored Content Images

Image spec: 1.91:1 ratio (1200x627px)We require 6x variations of this image: See the excel attached for the copy.Each image should contain the OSKEL logo, 2 headshots if posible, a designed background and a CTA button + the copy.Please make sure that all of the copy is clear and big enough to read so it can be read on mobile devices.

Target Market(s)

This is for Brellify ads to Executives of mid-market companies

Font styles to use
Sans Serif

Colors

Designer to choose colors to be used in the design.

```html
<!DOCTYPE html>
<html lang="en">
<head>
<meta charset="utf-8">
<title>OSKEL – Free Live Webinar</title>
<link rel="stylesheet" href="https://fonts.googleapis.com/css2?family=Raleway:wght@500;600;700;800&display=swap">
<style>
  :root {
    --navy-deep: #0a2a6b;
    --navy: #123a85;
    --blue-mid: #1f5cb8;
    --blue-bright: #3f8fe0;
    --band-fade: rgba(200, 218, 238, 0);
    --title-navy: #1b3563;
    --accent-orange: #f3a51c;
    --white: #ffffff;
    --headshot-left: #9fb7cf;
    --headshot-right: #b9c9da;
    --bottom-band: #0e3478;
  }
  * { margin: 0; padding: 0; box-sizing: border-box; }
  html, body { width: 1200px; height: 627px; overflow: hidden; }
  body { font-family: "Raleway", "Helvetica Neue", Arial, sans-serif; background: var(--navy-deep); }

  .ad-canvas {
    position: relative;
    width: 1200px;
    height: 627px;
    overflow: hidden;
    background:
      radial-gradient(ellipse 520px 360px at 330px 200px, rgba(90, 170, 240, 0.55), transparent 70%),
      linear-gradient(115deg, var(--blue-bright) 0%, var(--blue-mid) 35%, var(--navy) 65%, var(--navy-deep) 100%);
  }

  .headshot { position: absolute; border-radius: 2px; }
  .headshot--host { left: 0; top: 30px; width: 256px; height: 220px;
    background: linear-gradient(180deg, #c7d6e4 0%, var(--headshot-left) 100%); }
  .headshot--guest { left: 530px; top: 28px; width: 222px; height: 222px;
    background: linear-gradient(180deg, #dde6ef 0%, var(--headshot-right) 100%); }

  .brand {
    position: absolute;
    left: 850px;
    top: 70px;
    width: 300px;
    display: flex;
    align-items: center;
    justify-content: center;
    gap: 16px;
  }
  .brand__mark {
    width: 34px;
    height: 34px;
    background: var(--white);
  }
  .brand__name {
    font-size: 76px;
    font-weight: 700;
    line-height: 1;
    color: var(--white);
  }

  .info-band {
    position: absolute;
    left: 0;
    top: 250px;
    width: 1200px;
    height: 292px;
    background: linear-gradient(90deg, rgba(230, 238, 247, 0.92) 0%, rgba(222, 233, 245, 0.85) 45%, rgba(200, 218, 238, 0.55) 62%, var(--band-fade) 80%);
  }
  .info-band__content {
    position: absolute;
    left: 0;
    top: 0;
    width: 776px;
    text-align: center;
  }
  .eyebrow {
    margin-top: 12px;
    font-size: 47px;
    font-weight: 600;
    line-height: 56px;
    color: var(--accent-orange);
    letter-spacing: 1px;
  }
  .headline {
    margin-top: 26px;
    font-size: 33px;
    font-weight: 700;
    line-height: 40px;
    color: var(--title-navy);
    letter-spacing: 1.5px;
  }
  .subhead {
    margin-top: 14px;
    font-size: 22px;
    font-weight: 600;
    color: var(--title-navy);
    line-height: 29px;
    letter-spacing: 1.5px;
  }
  .subhead strong { font-weight: 800; }
  .event-date {
    margin-top: 20px;
    font-size: 28px;
    font-weight: 800;
    line-height: 34px;
    color: var(--accent-orange);
    letter-spacing: 1.5px;
  }

  .bottom-band {
    position: absolute;
    left: 0;
    top: 542px;
    width: 1200px;
    height: 85px;
    background: linear-gradient(90deg, var(--bottom-band) 0%, rgba(14, 52, 120, 0.6) 60%, rgba(14, 52, 120, 0) 100%);
  }
  .cta-button {
    position: absolute;
    left: 197px;
    top: 562px;
    width: 381px;
    height: 50px;
    border: 2px solid var(--white);
    background: var(--navy-deep);
    color: var(--white);
    font-size: 28px;
    font-weight: 700;
    letter-spacing: 1px;
    display: flex;
    align-items: center;
    justify-content: center;
    text-decoration: none;
  }
</style>
</head>
<body>
  <main class="ad-canvas">
    <div class="headshot headshot--host" role="img" aria-label="Headshot of the first webinar speaker in a light blue polo shirt"></div>
    <div class="headshot headshot--guest" role="img" aria-label="Headshot of the second webinar speaker in a white polo shirt"></div>

    <div class="brand">
      <span class="brand__mark"></span>
      <span class="brand__name">OSKEL</span>
    </div>

    <section class="info-band">
      <div class="info-band__content">
        <p class="eyebrow">FREE LIVE WEBINAR:</p>
        <h1 class="headline">"CYBERSECURITY STARTS AT THE TOP"</h1>
        <p class="subhead">HOW TO '<strong>SELL</strong>' A<br>CYBERSECURITY STRATEGY INTERNALLY</p>
        <p class="event-date">WEDNESDAY, JUNE 12TH AT 1PM EST</p>
      </div>
    </section>

    <div class="bottom-band"></div>
    <a class="cta-button" href="#">BOOK YOUR PLACE</a>
  </main>
</body>
</html>
```